Logo for hot realtor starting a team
The Lusk Team
Professional
Vernon Lusk III
See Attached photo
vernonlusk03@postlark.net
www.allbrackenvalehomesforsale.com
Slogan to be used - "Every Deal Closed By A Lusk"
Personal Picture and contact number
Reference draft #10 - I really like this one for a business card and I am looking for a new business card design and have a contest for this one. I will make sure to send you a request for a design. These are the changes that I would like to see and if you can make this happen, this is the winning business card, see below:
Change the style from cursive to manual script. Make the picture of what appears to be a Rose look more like a Rose. also make the font larger.
Remove the address completely and replace with my website (www.allbrackenvalehomesforsale.com and add contact number: 555-214-0386.
I would like the card to also be gray in color with black writing

```html
<!DOCTYPE html>
<html lang="en">
<head>
<meta charset="utf-8">
<title>The Lusk Team – Business Card</title>
<link href="https://fonts.googleapis.com/css2?family=Montserrat:wght@500&display=swap" rel="stylesheet">
<style>
  :root {
    --page-bg: #e4e4e2;
    --card-white: #ffffff;
    --band-black: #0c0c0c;
    --band-edge: #2a2a2a;
    --brand-red: #b3232a;
    --ink-dark: #1a1a1a;
    --ink-muted: #5a5a5a;
    --ink-light: #f2f2f2;
  }
  html, body {
    margin: 0;
    width: 1200px;
    height: 900px;
    overflow: hidden;
    background: var(--page-bg);
  }
  .canvas {
    position: relative;
    width: 1200px;
    height: 900px;
    display: flex;
    align-items: center;
    justify-content: center;
  }
  .business-card {
    position: relative;
    width: 1000px;
    height: 571px;
    background: var(--card-white);
    box-shadow: 0 10px 30px rgba(0,0,0,0.18);
    overflow: hidden;
  }
  .brand-lockup {
    position: absolute;
    left: 58px;
    top: 104px;
  }
  .brand-name {
    display: flex;
    align-items: center;
    gap: 14px;
    margin: 0;
    font-family: "Montserrat", Arial, sans-serif;
    font-weight: 500;
    font-size: 40px;
    letter-spacing: 1px;
    color: var(--ink-dark);
    line-height: 1;
  }
  .brand-mark {
    width: 20px;
    height: 20px;
    background: var(--brand-red);
  }
  .brand-slogan {
    margin: 14px 0 0 36px;
    font-family: "Montserrat", Arial, sans-serif;
    font-weight: 500;
    font-size: 16px;
    letter-spacing: 1.5px;
    color: var(--ink-muted);
  }
  .info-band {
    position: absolute;
    left: 0;
    right: 0;
    top: 250px;
    height: 222px;
    background: linear-gradient(180deg, var(--band-edge) 0, var(--band-black) 8px, var(--band-black) 100%);
  }
  .agent-name {
    position: absolute;
    right: 46px;
    top: 82px;
    margin: 0;
    font-family: "Montserrat", Arial, sans-serif;
    font-weight: 500;
    font-size: 22px;
    letter-spacing: 4px;
    font-variant: small-caps;
    color: var(--ink-light);
  }
  .contact-list {
    position: absolute;
    left: 40px;
    bottom: 22px;
    margin: 0;
    padding: 0;
    list-style: none;
  }
  .contact-item {
    display: flex;
    align-items: center;
    gap: 10px;
    height: 25px;
    font-family: "Montserrat", Arial, sans-serif;
    font-weight: 500;
    font-size: 14px;
    letter-spacing: 2px;
    text-transform: uppercase;
    color: var(--ink-light);
  }
  .contact-icon {
    width: 17px;
    height: 17px;
    flex: none;
  }
</style>
</head>
<body>
<div class="canvas">
  <article class="business-card">
    <header class="brand-lockup">
      <p class="brand-name"><span class="brand-mark"></span>The Lusk Team</p>
      <p class="brand-slogan">Every Deal Closed By A Lusk</p>
    </header>

    <section class="info-band">
      <h1 class="agent-name">Vernon Lusk III</h1>
      <ul class="contact-list">
        <li class="contact-item">
          <svg class="contact-icon" viewBox="0 0 20 20"><circle cx="10" cy="10" r="10" fill="#f2f2f2"/><path d="M6.5 5.5l2 0 1 2.5-1.3 1a6 6 0 0 0 2.8 2.8l1-1.3 2.5 1 0 2a1 1 0 0 1-1 1A8 8 0 0 1 5.5 6.5a1 1 0 0 1 1-1z" fill="#0c0c0c"/></svg>
          555-309-1742
        </li>
        <li class="contact-item">
          <svg class="contact-icon" viewBox="0 0 20 20"><circle cx="10" cy="10" r="10" fill="#f2f2f2"/><rect x="7" y="4.5" width="6" height="11" rx="1" fill="#0c0c0c"/><rect x="8" y="6" width="4" height="7" fill="#f2f2f2"/></svg>
          555-214-0386
        </li>
        <li class="contact-item">
          <svg class="contact-icon" viewBox="0 0 20 20"><circle cx="10" cy="10" r="10" fill="#f2f2f2"/><rect x="5" y="6.5" width="10" height="7" fill="#0c0c0c"/><path d="M5 6.5l5 4 5-4" fill="none" stroke="#f2f2f2" stroke-width="1"/></svg>
          vernonlusk03@postlark.net
        </li>
        <li class="contact-item">
          <svg class="contact-icon" viewBox="0 0 20 20"><circle cx="10" cy="10" r="10" fill="#f2f2f2"/><circle cx="10" cy="10" r="5" fill="none" stroke="#0c0c0c" stroke-width="1.3"/><ellipse cx="10" cy="10" rx="2" ry="5" fill="none" stroke="#0c0c0c" stroke-width="1.1"/><line x1="5" y1="10" x2="15" y2="10" stroke="#0c0c0c" stroke-width="1.1"/></svg>
          www.allbrackenvalehomesforsale.com
        </li>
      </ul>
    </section>
  </article>
</div>
</body>
</html>
```